Corinne Bracket tutoring Advertising package - flyers, posters, business card and logo

I am looking for a flyer design for my tutoring business, it needs to explain what tutoring services I offer, how much I charge, why my services are worthwhile, it should include some photos of me and the tutoring centre,

It needs to include my phone number and my website. It should quote from some of the testimonials I have received from parents and children.

My website is www.corinnebracket-example.com My Facebook page can be found at https://www.facebook.com/corinnebrackettutoring These pages include a range of photos and quotes that you can use.

I am not sure about the colours and designs that I would like, that's why I'm using Sketchmarket!
I'm looking to appeal to parents inform them of my skills and experience.

I'm charging $45 for sessions of an hour and 15 minutes. 2 sessions per week will cost $80. I tutor Monday to Friday afternoons and evenings along with all day Saturdays. The assessment is free.

I tutor children from K-9 in English and Maths. I'm mainly aiming at parents whose children are struggling a little bit at school although I can help children who are doing well too.
I am highly skilled at helping children who can't read, I have a comprehensive program, the Pemberly program, that specifically teaches children the skills they need to read fluently and successfully.

Similarly I have had a lot of experience at helping children improve their Maths skills. I am well resourced with a wide range of hands on resources, paper resources and electronic resources.

Children will get better GRESTO results if I tutor them (GRESTO is the national series of tests in Australia).

I'm after a DL double sided flyer, and an A4 flyer. I'm also looking for two A2 posters and two A3 posters. Finally, I want a business card too. I don't have a logo for the business and I'd love to have one!

Target Market(s)

Parents of school aged children

Industry/Entity Type

Education

Colors

Designer to choose colors to be used in the design.

Requirements
Must have
• my name, my photo, length and cost of my sessions, email and phone contact details. Subjects and age ranges that I teach, times that I tutor. Website and/or Facebook page references. Quotes from Testimonials
Nice to have
• The A2 and A3 posters should complement each other.

```html
<!DOCTYPE html>
<html lang="en">
<head>
<meta charset="utf-8">
<title>Corinne Bracket Tutoring – A4 Flyer</title>
<link rel="stylesheet" href="https://fonts.googleapis.com/css2?family=Ubuntu:wght@400;500;700&display=swap">
<style>
  :root {
    --red: #d71f26;
    --red-deep: #a3141a;
    --red-dark: #7d0e12;
    --ink: #3a3a3a;
    --black: #111111;
    --charcoal: #2b2b2b;
    --white: #ffffff;
    --wall: #e9e6df;
    --shirt: #7fb55a;
  }
  * { margin: 0; padding: 0; box-sizing: border-box; }
  html, body { width: 871px; height: 1200px; overflow: hidden; background: var(--white); }
  body { font-family: "Ubuntu", sans-serif; color: var(--ink); }

  .flyer { position: relative; width: 871px; height: 1200px; background: var(--white); overflow: hidden; }

  .header-art { position: absolute; left: 0; top: 0; width: 871px; height: 700px; }

  .headline {
    position: absolute; left: 70px; top: 40px; width: 731px;
    color: var(--white); font-weight: 500; font-size: 32.5px; line-height: 38.5px;
    text-align: center;
  }

  .details { position: absolute; left: 26px; top: 711px; width: 510px; }
  .details p { font-size: 15px; line-height: 19.3px; margin-bottom: 21px; color: var(--ink); }
  .details p.tight { margin-bottom: 16px; }

  .contact {
    position: absolute; left: 26px; top: 988px; width: 525px;
    font-size: 11.5px; line-height: 15px; color: var(--ink);
  }
  .contact strong { color: var(--red); font-weight: 700; }

  .portrait {
    position: absolute; left: 564px; top: 676px; width: 277px; height: 296px;
    border: 4px solid var(--red); border-radius: 16px; overflow: hidden;
    background: linear-gradient(160deg, var(--wall) 0%, #c9b79c 40%, var(--shirt) 100%);
  }
  .nameplate {
    position: absolute; left: 585px; top: 972px; width: 238px; height: 36px;
    background: linear-gradient(#2f2f2f, var(--black));
    clip-path: polygon(0 0, 100% 0, 94% 100%, 6% 100%);
    color: var(--white); font-size: 22px; font-weight: 500;
    display: flex; align-items: center; justify-content: center;
  }

  .divider-red { position: absolute; left: 0; top: 1031px; width: 871px; height: 6px; background: linear-gradient(90deg, var(--red-dark), var(--red), var(--red-dark)); }
  .divider-white { position: absolute; left: 0; top: 1037px; width: 871px; height: 5px; background: var(--white); }

  .testimonials {
    position: absolute; left: 0; top: 1042px; width: 871px; height: 158px;
    background: linear-gradient(180deg, var(--black) 0%, var(--charcoal) 100%);
    color: var(--white); padding: 20px 26px 0 26px;
  }
  .testimonials h2 { font-size: 16px; font-weight: 700; margin-bottom: 9px; }
  .quote { font-size: 10.3px; line-height: 13.5px; letter-spacing: -0.15px; }
  .quote-author { font-size: 13px; font-weight: 500; margin: 2px 0 12px; }
</style>
</head>
<body>
<main class="flyer">

  <svg class="header-art" viewBox="0 0 871 700">
    <defs>
      <linearGradient id="headerRed" x1="0" y1="0" x2="1" y2="1">
        <stop offset="0" stop-color="#c4161c"/>
        <stop offset="0.55" stop-color="#d71f26"/>
        <stop offset="1" stop-color="#8f1015"/>
      </linearGradient>
      <linearGradient id="ringDark" x1="0" y1="0" x2="0" y2="1">
        <stop offset="0" stop-color="#555"/>
        <stop offset="1" stop-color="#0d0d0d"/>
      </linearGradient>
      <linearGradient id="roomA" x1="0" y1="0" x2="1" y2="1">
        <stop offset="0" stop-color="#e8e4da"/>
        <stop offset="0.45" stop-color="#b9803f"/>
        <stop offset="1" stop-color="#7b4d26"/>
      </linearGradient>
      <linearGradient id="roomB" x1="0" y1="0" x2="1" y2="1">
        <stop offset="0" stop-color="#ecebe5"/>
        <stop offset="0.5" stop-color="#a8693a"/>
        <stop offset="1" stop-color="#3a3f4a"/>
      </linearGradient>
      <linearGradient id="roomC" x1="0" y1="0" x2="1" y2="1">
        <stop offset="0" stop-color="#ddd9cf"/>
        <stop offset="0.6" stop-color="#8d6a4a"/>
        <stop offset="1" stop-color="#3b3430"/>
      </linearGradient>
    </defs>

    <path d="M0 0 H871 V212 C800 226 740 250 680 290 L560 300 C420 300 250 320 0 356 Z" fill="url(#headerRed)"/>
    <path d="M0 356 C250 320 420 300 560 300 L680 290 C740 250 800 226 871 212 V232 C800 246 745 268 690 305 L560 318 C420 318 250 336 0 372 Z" fill="#8f1015" opacity="0.55"/>
    <path d="M0 250 C120 300 220 330 320 360 L300 372 C200 340 90 310 0 290 Z" fill="#ffffff" opacity="0.12"/>

    <circle cx="250" cy="452" r="214" fill="url(#ringDark)"/>
    <circle cx="250" cy="452" r="204" fill="var(--red)"/>
    <circle cx="250" cy="452" r="197" fill="url(#roomA)" role="img" aria-label="Photo of the tutoring room with wooden bookshelves, a desk and blue chairs"/>

    <circle cx="640" cy="404" r="165" fill="url(#ringDark)"/>
    <circle cx="640" cy="404" r="157" fill="var(--red)"/>
    <circle cx="640" cy="404" r="151" fill="url(#roomB)" role="img" aria-label="Photo of the tutoring centre with a large table and shelves of books"/>

    <circle cx="517" cy="577" r="112" fill="url(#ringDark)"/>
    <circle cx="517" cy="577" r="105" fill="var(--red)"/>
    <circle cx="517" cy="577" r="100" fill="url(#roomC)" role="img" aria-label="Photo of bookshelves in a corner of the tutoring centre"/>
  </svg>

  <h1 class="headline">I tutor children from K-9 in English and Maths. I'm mainly aiming at parents whose children are struggling a little bit at school although I can help children who are doing well too.</h1>

  <section class="details">
    <p>I'm charging $45 for sessions of an hour and 15 minutes. 2 sessions per week will cost $80. I tutor Monday to Friday afternoons and evenings along with all day Saturdays. The assessment is free.</p>
    <p>I am highly skilled at helping children who can't read, I have a comprehensive program, the Pemberly program, that specifically teaches children the skills they need to read fluently and successfully.</p>
    <p class="tight">Similarly I have had a lot of experience at helping children improve their Maths skills. I am well resourced with a wide range of hands on resources, paper resources and electronic resources.</p>
    <p>Children will get better GRESTO results if I tutor them (GRESTO is the national series of tests in Australia).</p>
  </section>

  <address class="contact">
    <strong>Phone:</strong> (02) 5550 1234 &nbsp; <strong>Email:</strong> hello@corinnebracket-example.com &nbsp; <strong>Web:</strong> www.corinnebracket-example.com<br>
    <strong>Facebook:</strong> https://www.facebook.com/corinnebrackettutoring
  </address>

  <div class="portrait" role="img" aria-label="Portrait photo of the tutor in front of a bookshelf"></div>
  <div class="nameplate">CORINNE BRACKET</div>

  <div class="divider-red"></div>
  <div class="divider-white"></div>

  <section class="testimonials">
    <h2>Testimonials:</h2>
    <p class="quote">Our son has been tutored by Corinne now for the past 2 years - we have noticed a big improvement with his spelling and mathematics. This has also helped our son's confidence in his daily schooling and he now has started to enjoy school again . Thanks Corinne</p>
    <p class="quote-author">Dean and Priya Holloway</p>
    <p class="quote">Our children love going to Corinne's!! Yes you read that right - they LOVE going to learn! Corinne has the ability to tap into each child's strengths and weaknesses and she makes learning fun! Our children's grades have improved more so, our son just got awarded a distinction in a science competition! Thanks so much Corinne.</p>
    <p class="quote-author">Maree Tansley</p>
  </section>

</main>
</body>
</html>
```